Design Contest: A New Look & Feel for MORVEK.nl

🌍 Context
MORVEK.nl combines knowledge about supplements, ingredients, and spirituality, while also offering lectures, retreats, and training programs.
We are not a foundation or donation platform, but an open knowledge network with a professional, warm, and trustworthy presence.

Our mission is to connect science and soul, sharing valuable insights and experiences that inspire both rational understanding and spiritual growth.

🎯 The Goal
We’re inviting talented web designers and visual creatives to redesign MORVEK.nl into a modern, elegant, and emotionally resonant platform.

The new design should communicate:
Warmth and human connection,
Professionalism and clarity, and
A sense of discovery and inspiration.
The site will serve as a central hub for education, community, and conscious travel β€” bridging science, nature, and spirituality.

Landing Page (One-Pager):

A welcoming introduction to MORVEK that immediately conveys our essence: knowledge, connection, and inspiration.
Visually guides visitors toward our main areas β€” journeys, education, and knowledge β€” with clear calls to action.

Travel Page Design:

A dedicated layout for a spiritual journey or retreat
Should evoke curiosity, emotion, and trust β€” encouraging visitors to read the program and feel inspired to book.

Education Page Design:
A page for one specific training or lecture.
Should look professional and engaging, highlighting benefits and making visitors eager to sign up.

Ingredient Page Design:
A clean, structured layout for an ingredient (e.g., Tralinex Q7 Blend®).
Should balance science and accessibility β€” informative yet visually appealing, showing related insights or products.

✨ What We’re Looking For
🌸 Warm, Friendly Aesthetic
A soft, grounded color palette (see moodboard below).
A look that feels welcoming, safe, modern, and inspiring.
Avoid harsh contrasts or corporate coldness β€” aim for organic elegance and heart-centered design.

🌿 Clean, Airy Layout
Generous white/cream space for readability and calm.
Rounded corners, smooth transitions, and balanced composition.
Use light textures (paper, waves, or organic shapes) to evoke warmth.

✍️ Modern Typography
Body text: Nunito, Lato, or Raleway β€” friendly, clear, and easy to read.
Headings: Playfair Display or Quicksand β€” elegant and expressive.
Typography should reflect both expertise and approachability.

πŸ”— Clear Navigation
Logical, intuitive structure with the following key areas:
Knowledge Hub – Products – Activities – About – Contact
Clear, soft-toned buttons and navigation encouraging exploration.
Consider β€œrelated content” cards or visual pathways connecting knowledge, events, and products.

πŸ’« Visual Integration
Create visual links between knowledge, activities, and products (e.g., tags, badges, or modular cards).
Filters or category highlights to navigate supplement/ingredient content easily.
Visual flow should feel alive yet harmonious.

🧠 Local & Human Connection
Photography that emphasizes real people, learning moments, and connection with nature.
Avoid clinical or corporate stock images β€” show authenticity, empathy, and light.

🀝 Community Features
Dedicated space for reviews, expert Q&A, or interaction.
These areas should radiate trust, safety, and a sense of belonging.

🧩 Plonk CMS Compatibility
Must be responsive and easily built within Plonk CMS (drag-and-drop).
Show where dynamic content (articles, events, or journeys) will be placed and how cards adapt to different devices.

🎨 Moodboard & Color Palette
Color Name HEX Code Emotion & Use
Warm Beige #DFBAAA The grounding base color β€” evokes natural warmth, balance, and calm. Ideal for backgrounds and section dividers.
Light Cream #F5EAE5 Airy and gentle β€” conveys purity, openness, and readability. Use for backgrounds and whitespace.
Deep Aubergine #431624 Adds depth and mystery β€” perfect for headlines, highlights, or footers. Symbolizes introspection and wisdom.
Wine Red #750E2B Expresses vitality, heart energy, and focus. Ideal for buttons, accents, or key highlights.
Burnt Orange #F26C2E Brings creative spark and positivity. Great for hover states, subtle icons, or energetic accents.
Mustard Yellow #B68620 Symbolizes light, optimism, and knowledge. Use as a secondary accent or highlight.

Color philosophy:
This palette represents the meeting point between Earth and Fire β€” grounding warmth combined with vibrant inspiration.
It visually communicates the essence of MORVEK: trustworthy science, human connection, and transformative energy.

🧠 Target Audience
Health professionals and therapists seeking supplement and ingredient education.
Consumers and conscious individuals interested in wellbeing, spirituality, and science.
Spiritual explorers looking for transformative journeys and community learning.

πŸ’‘ Functional & Structural Goals
The site should clearly showcase MORVEK’s four pillars:
Journeys & Retreats – spiritual travel experiences.
Academy & Trainings – professional education and lectures.
Knowledge Center – accessible supplement & ingredient knowledge (scientific yet warm).

πŸ“¦ What to Submit
A homepage concept (desktop + mobile).
Final delivery as a layererd PSD

```html
<!DOCTYPE html>
<html lang="en">
<head>
<meta charset="utf-8">
<title>MORVEK — Bridge Science. Awaken Soul.</title>
<link rel="stylesheet" href="https://fonts.googleapis.com/css2?family=Playfair+Display:wght@600;700&family=Poppins:wght@400;500;600&display=swap">
<style>
:root{
  --wine:#750E2B;
  --aubergine:#431624;
  --mustard:#B68620;
  --beige:#DFBAAA;
  --cream:#F5EAE5;
  --paper:#EBD6CA;
  --panel:#F1E4DA;
  --blush:#F6E4E2;
  --ink:#1b1416;
  --text:#4a3a38;
  --field:#f1eeee;
}
*{margin:0;padding:0;box-sizing:border-box}
html,body{width:1200px;height:4950px;overflow:hidden}
body{position:relative;background:var(--paper);font-family:'Poppins',sans-serif;color:var(--ink)}
.abs{position:absolute}
.serif{font-family:'Playfair Display',serif;font-weight:700}
.accent{color:var(--wine)}
.btn{position:absolute;display:flex;align-items:center;justify-content:center;border-radius:24px;font-size:12px;font-weight:600;letter-spacing:.2px;text-transform:uppercase}
.btn-wine{background:var(--wine);color:#fff}
.btn-outline{background:var(--cream);border:2px solid var(--ink);color:var(--ink)}
.btn-mustard{background:var(--mustard);color:#fff;border:2px solid #6b4a0f}

/* hero */
.hero{left:0;top:0;width:1200px;height:646px;background:linear-gradient(100deg,#e9b48e 0%,#d98d5d 38%,#b8613a 62%,#8f4a2d 100%)}
.hero-photo{left:560px;top:0;width:640px;height:646px;background:radial-gradient(ellipse at 40% 40%,#f0c9a4 0%,#c97a4c 45%,rgba(143,74,45,0) 80%)}
.logo{left:144px;top:36px;display:flex;align-items:center;gap:10px;font-size:22px;font-weight:600;color:var(--wine)}
.logo-mark{width:30px;height:30px;border-radius:50%;background:var(--wine)}
.nav{left:560px;top:44px;display:flex;gap:29px;font-size:13px;font-weight:500}
.hero-title{left:142px;top:190px;font-size:50px;line-height:54px;color:var(--ink)}

/* explore */
.section-title{width:1200px;left:0;text-align:center;font-size:38px}
.card-img{width:298px;height:225px;border-radius:6px}
.card-title{width:340px;text-align:center;font-size:13px;font-weight:500;text-transform:uppercase}
.card-text{width:340px;text-align:center;font-size:13px;line-height:26px;color:var(--text)}

/* science */
.science{left:19px;top:1432px;width:1160px;height:743px;background:var(--panel);border-radius:6px}
.tab{font-size:12px;height:46px}
.sci-head{left:125px;top:1712px;width:470px;font-size:13px;font-weight:600;line-height:25px;text-transform:uppercase}
.sci-text{left:127px;top:1780px;width:450px;font-size:12.5px;line-height:25.6px;color:var(--text)}
.sci-img{left:644px;top:1629px;width:458px;height:411px;border-radius:6px;background:linear-gradient(135deg,#dbe9e0 0%,#a9c9b2 35%,#8e4a2f 70%,#5e2a18 100%)}

/* testimonials */
.avatar{left:531px;top:2367px;width:138px;height:138px;border-radius:50%;background:radial-gradient(circle,#f3c3a0 0%,#e79a6e 100%)}
.t-name{width:1200px;left:0;top:2544px;text-align:center;font-size:15px;font-weight:500}
.t-text{left:200px;top:2582px;width:800px;text-align:center;font-size:13px;line-height:26px;color:var(--text)}
.dots{left:490px;top:2694px;display:flex;gap:20px}
.dot{width:16px;height:16px;border-radius:50%;background:#eee2dc}
.dot.on{background:var(--mustard)}

/* about */
.about-img{left:121px;top:2871px;width:458px;height:448px;border-radius:6px;background:linear-gradient(160deg,#e9b15b 0%,#a66a3c 45%,#5a3a2a 100%)}
.about-title{left:658px;top:2860px;font-size:38px}
.about-text{left:658px;width:450px;font-size:12.5px;line-height:25.8px;color:var(--text)}

/* faq */
.faq-bg{left:0;top:3481px;width:1200px;height:710px;background:linear-gradient(180deg,var(--panel),#f0e0d6)}
.faq{left:204px;width:790px;height:64px;border-radius:32px;background:#fff;display:flex;align-items:center;justify-content:space-between;padding:0 48px 0 36px;font-size:14px;font-weight:600}
.faq-icon{width:14px;height:14px}

/* mission / contact */
.blush-bg{left:0;top:4191px;width:1200px;height:759px;background:var(--blush)}
.mission{left:117px;top:4119px;width:977px;height:177px;background:#f8e6e4;border-radius:4px;box-shadow:0 6px 20px rgba(120,60,50,.08)}
.mission h2{position:absolute;left:96px;top:22px;font-size:38px}
.mission p{position:absolute;left:98px;top:94px;width:700px;font-size:12.5px;line-height:25px;color:var(--text)}
.form{left:117px;top:4394px;width:508px;height:448px;background:#fff;border-radius:4px}
.field{left:175px;width:356px;border-radius:24px;background:var(--field);font-size:12.5px;color:#8a7d7d;padding:14px 22px}
.contact-title{left:731px;top:4496px;font-size:38px}
.contact-hq{left:731px;top:4575px;font-size:16px;font-weight:500}
.contact-text{left:734px;top:4609px;width:380px;font-size:12.5px;line-height:25px;color:var(--text)}
.copyright{width:1200px;left:0;top:4884px;text-align:center;font-size:13px}
</style>
</head>
<body>

<header>
  <div class="abs hero"></div>
  <div class="abs hero-photo" role="img" aria-label="Photo of a smiling woman in a sun hat in a golden field at sunset"></div>
  <div class="abs logo"><span class="logo-mark"></span>MORVEK</div>
  <nav class="abs nav"><span>KNOWLEDGE HUB</span><span>PRODUCTS</span><span>ACTIVITIES</span><span>ABOUT</span><span>CONTACT</span></nav>
  <h1 class="abs serif hero-title">Bridge Science.<br>Awaken Soul.<br>Connect with MORVEK</h1>
  <a class="btn btn-wine" style="left:142px;top:396px;width:268px;height:44px">Visit the Knowledge Hub</a>
  <a class="btn btn-outline" style="left:415px;top:396px;width:227px;height:44px">Explore our Journeys</a>
</header>

<section class="explore">
  <h2 class="abs serif section-title" style="top:766px">Explore the <span class="accent">MORVEK Experience</span></h2>

  <div class="abs card-img" style="left:92px;top:852px;background:linear-gradient(180deg,#e58d6b,#5d2b27)" role="img" aria-label="Photo of a person reading on a bench at dawn"></div>
  <div class="abs card-img" style="left:450px;top:852px;background:linear-gradient(180deg,#f2c9a0,#8d5a46)" role="img" aria-label="Photo of many hands joined together"></div>
  <div class="abs card-img" style="left:808px;top:852px;background:linear-gradient(180deg,#e7d2c6,#9f8377)" role="img" aria-label="Photo of a woman resting with a travel pillow"></div>

  <div class="abs card-title" style="left:72px;top:1106px">Knowledge Hub</div>
  <div class="abs card-title" style="left:430px;top:1106px">Academy &amp; Training</div>
  <div class="abs card-title" style="left:788px;top:1106px">Journeys &amp; Retreats</div>

  <p class="abs card-text" style="left:72px;top:1138px">Explore our expert-curated library of supplement and ingredient insights. Scientific, trustworthy, and always warm</p>
  <p class="abs card-text" style="left:430px;top:1138px">Elevate your practice. Access expert lectures, deep-dive courses, and certifications for holistic health professionals.</p>
  <p class="abs card-text" style="left:788px;top:1138px">Join transformative, heart-centered retreats that connect you with nature, community, and deeper spiritual insights.Find Your Journey</p>

  <a class="btn btn-mustard" style="left:125px;top:1242px;width:235px;height:45px">Explore the Science</a>
  <a class="btn btn-mustard" style="left:481px;top:1242px;width:235px;height:45px">View all Programs</a>
  <a class="btn btn-mustard" style="left:837px;top:1242px;width:235px;height:45px">Find your Journey</a>
</section>

<section>
  <div class="abs science"></div>
  <h2 class="abs serif section-title" style="top:1528px">Science &amp; <span class="accent">Soul in Focus</span></h2>
  <a class="btn btn-wine tab" style="left:119px;top:1629px;width:235px">Tralinex Q7 Blend®</a>
  <a class="btn btn-outline tab" style="left:365px;top:1629px;width:229px;text-transform:uppercase">The Power of Grounding</a>
  <h3 class="abs sci-head">Research review of Tralinex's immune benefits by Norvell founder Dr. Aram Velden published</h3>
  <p class="abs sci-text">Lorem ipsum dolor sit amet, consectetur adipiscing elit, sed do eiusmod tempor incididunt ut labore et dolore magna aliqua. Ut enim ad minim veniam, quis nostrud exercitation ullamco laboris nisi ut aliquip ex ea commodo consequat. Duis aute irure dolor in reprehenderit in voluptate velit esse cillum dolore eu fugiat nulla pariatur. Excepteur sint occaecat cupidatat non</p>
  <a class="btn btn-mustard" style="left:119px;top:1958px;width:235px;height:44px">Read More</a>
  <div class="abs sci-img" role="img" aria-label="Product photo of a skincare jar and amber pump bottle among green leaves"></div>
</section>

<section>
  <h2 class="abs serif section-title" style="top:2266px">Our <span class="accent">Testimonials</span></h2>
  <div class="abs avatar" role="img" aria-label="Portrait of a smiling customer"></div>
  <div class="abs t-name">LENA VARRO</div>
  <p class="abs t-text">Lorem ipsum dolor sit amet, consectetur adipiscing elit, sed do eiusmod tempor incididunt ut labore et dolore magna aliqua. Ut enim ad minim veniam, quis nostrud exercitation ullamco laboris nisi ut aliquip ex ea commodo consequat. Duis aute irure dolor in reprehenderit in voluptate velit esse cillum dolore eu</p>
  <div class="abs dots"><span class="dot"></span><span class="dot"></span><span class="dot"></span><span class="dot"></span><span class="dot on"></span><span class="dot"></span><span class="dot"></span></div>
</section>

<section>
  <div class="abs about-img" role="img" aria-label="Photo of a laughing older couple walking through an autumn street"></div>
  <h2 class="abs serif about-title">About <span class="accent">Us</span></h2>
  <p class="abs about-text" style="top:2928px">Lorem ipsum dolor sit amet, consectetur adipiscing elit, sed do eiusmod tempor incididunt ut labore et dolore magna aliqua. Ut enim ad minim veniam, quis nostrud exercitation ullamco laboris nisi ut aliquip ex ea commodo consequat. Duis aute irure dolor in reprehenderit in voluptate velit esse cillum dolore eu fugiat nulla pariatur. Excepteur sint occaecat cupidatat non proident, sunt in culpa qui officia deserunt mollit anim id est laborum.</p>
  <p class="abs about-text" style="top:3132px">Lorem ipsum dolor sit amet, consectetur adipiscing elit, sed do eiusmod tempor incididunt ut labore et dolore magna aliqua. Ut enim ad minim veniam, quis nostrud exercitation ullamco laboris nisi ut aliquip ex ea commodo consequat. Duis aute irure dolor in reprehenderit in voluptate velit esse cillum dolore eu fugiat nulla pariatur. Excepteur sint occaecat cupidatat non proident, sunt in culpa qui officia deserunt mollit anim id est laborum.</p>
</section>

<section>
  <div class="abs faq-bg"></div>
  <h2 class="abs serif section-title" style="top:3578px">Any <span class="accent">Questions</span></h2>
  <div class="abs faq" style="top:3665px"><span>1. Lorem ipsum dolor sit amet, consectetur adipiscing elit ?</span><svg class="faq-icon" viewBox="0 0 14 14"><circle cx="7" cy="7" r="7" fill="var(--aubergine)"/><path d="M6 4l3 3-3 3" stroke="#fff" stroke-width="1.6" fill="none"/></svg></div>
  <div class="abs faq" style="top:3753px"><span>2. Lorem ipsum dolor sit amet, consectetur adipiscing elit ?</span><svg class="faq-icon" viewBox="0 0 14 14"><circle cx="7" cy="7" r="7" fill="var(--aubergine)"/><path d="M6 4l3 3-3 3" stroke="#fff" stroke-width="1.6" fill="none"/></svg></div>
  <div class="abs faq" style="top:3840px"><span>3. Lorem ipsum dolor sit amet, consectetur adipiscing elit ?</span><svg class="faq-icon" viewBox="0 0 14 14"><circle cx="7" cy="7" r="7" fill="var(--aubergine)"/><path d="M6 4l3 3-3 3" stroke="#fff" stroke-width="1.6" fill="none"/></svg></div>
  <div class="abs faq" style="top:3928px"><span>4. Lorem ipsum dolor sit amet, consectetur adipiscing elit ?</span><svg class="faq-icon" viewBox="0 0 14 14"><circle cx="7" cy="7" r="7" fill="var(--aubergine)"/><path d="M6 4l3 3-3 3" stroke="#fff" stroke-width="1.6" fill="none"/></svg></div>
</section>

<div class="abs blush-bg"></div>

<section class="abs mission">
  <h2 class="serif">Our <span class="accent">Mission</span></h2>
  <p>Our mission is to connect science and soul, sharing valuable insights and experiences that inspire both rational understanding and spiritual growth.</p>
</section>

<section>
  <div class="abs form"></div>
  <div class="abs field" style="top:4454px;height:46px">Name</div>
  <div class="abs field" style="top:4511px;height:47px">Email Address</div>
  <div class="abs field" style="top:4577px;height:161px;border-radius:18px">Message</div>
  <a class="btn btn-wine" style="left:175px;top:4756px;width:356px;height:44px">Submit</a>

  <h2 class="abs serif contact-title">Contact <span class="accent">Us</span></h2>
  <div class="abs contact-hq">MORVEK HEADQUARTERS</div>
  <p class="abs contact-text">Based in the Netherlands — connecting globally through knowledge and spirit.<br><span style="display:block;margin-top:7px">Email: info@morvek.nl</span>Phone: +31 (0) 6 987 654 32</p>
</section>

<footer class="abs copyright">Copyright@2025.All Rights Rserved</footer>

</body>
</html>
```